Willowmere Surgery Brochure Design

Willowmere Surgery (willowmeresurgery.example)

Is a comprehensive breast care center that focuses on caring for women with breast cancer and other breast pathologies. We need a promotional and marketing brochure, in a tri-fold format, to provide information about our office and describe the services that we offer.

Deliverable

* The brochure should be completed by August 24th
* We will need the necessary files to get the brochure printed (.ai, .indd, etc).

Target Market(s)

Primarily patients of age between 30+ and 70+. The brochure will also be placed in doctor's waiting room

Industry/Entity Type

Marketing

Requirements
Must have
• * Make use of the color scheme as the website (http://willowmeresurgery.example, http://willowmeresurgery.example/static/theme-fuchsia.png)
* Incorporate the following graphic elements:
* The company’s logo (provided as an attachment)
* At least one images from the homepage
* Photos of the primary doctor and her staff
* Map to show the office location and phone number
* Enclose a breast cancer self-exam card (http://willowmeresurgery.example/static/shower-card.jpg)
* A portion of the brochure must be detachable and serve as business cards that can be cut off (see attachment).
Nice to have
• Here is an example of a brochure that we like:

http://plakmarket.example/item/flexible-trifold-brochure/731284?WT.ac=search_item&WT.seg_1=search_item&WT.z_author=dembrovi

```html
<!DOCTYPE html>
<html lang="en">
<head>
<meta charset="utf-8">
<title>Willowmere Surgery – Comprehensive Breast Care</title>
<link href="https://fonts.googleapis.com/css2?family=Arimo:ital,wght@0,400;0,700;1,400&display=swap" rel="stylesheet">
<style>
  :root {
    --pink-light: #dc94b6;
    --pink-deep: #a85680;
    --maroon: #7c3552;
    --maroon-dark: #5f2640;
    --white: #ffffff;
    --ink: #111111;
    --guide: #b9b9b9;
    --logo-pink: #f2a9c9;
  }
  html, body { margin: 0; padding: 0; overflow: hidden; background: var(--white); }
  .brochure {
    position: relative;
    width: 1200px; height: 933px;
    overflow: hidden;
    font-family: "Arimo", Arial, sans-serif;
    color: var(--ink);
  }
  .backdrop { position: absolute; inset: 0; }
  .guide-label {
    position: absolute; font-size: 11px; font-weight: 700; color: var(--guide);
    letter-spacing: .2px; white-space: nowrap;
  }
  .fold-label {
    position: absolute; font-size: 11px; font-weight: 700; color: #d6d6d6;
    transform: rotate(-90deg); transform-origin: left top; white-space: nowrap;
  }
  .photo { position: absolute; }
  .panel { position: absolute; font-size: 8.6px; line-height: 10px; }
  .panel p { margin: 0 0 10px; }
  .panel ul { list-style: none; margin: 0; padding: 0; }
  .panel ul + ul { margin-top: 2px; }
  .panel-comprehensive { left: 32px; top: 413px; width: 366px; font-size: 8.9px; line-height: 11px; }
  .panel-comprehensive p { margin-bottom: 11px; }
  .panel-personal { left: 412px; top: 228px; width: 372px; }
  .panel-personal .closing { margin-top: 19px; }
  .panel-timely { left: 800px; top: 262px; width: 362px; }
  .brand {
    position: absolute; left: 826px; top: 786px;
    display: flex; align-items: center; gap: 6px;
  }
  .brand-mark { width: 10px; height: 10px; border-radius: 50%; background: var(--logo-pink); }
  .brand-name { font-size: 20px; color: var(--logo-pink); font-weight: 400; letter-spacing: .3px; }
  .brand-tagline {
    position: absolute; left: 1006px; top: 816px;
    font-size: 11px; font-style: italic; color: var(--white);
  }
</style>
</head>
<body>
<div class="brochure">

  <svg class="backdrop" width="1200" height="933" viewBox="0 0 1200 933" aria-hidden="true">
    <defs>
      <linearGradient id="topBand" x1="0" y1="0" x2="0" y2="1">
        <stop offset="0" stop-color="#dc94b6"/>
        <stop offset="1" stop-color="#a85680"/>
      </linearGradient>
      <linearGradient id="bottomBand" x1="0" y1="0" x2="0" y2="1">
        <stop offset="0" stop-color="#7c3552"/>
        <stop offset="1" stop-color="#5f2640"/>
      </linearGradient>
      <linearGradient id="lotusTone" x1="0" y1="0" x2="0" y2="1">
        <stop offset="0" stop-color="#e9b9cb"/>
        <stop offset="1" stop-color="#cf8ea9"/>
      </linearGradient>
      <linearGradient id="cardTone" x1="0" y1="0" x2="1" y2="0">
        <stop offset="0" stop-color="#e86a98"/>
        <stop offset="1" stop-color="#f4c2d4"/>
      </linearGradient>
    </defs>
    <path d="M0 0 H1200 V230 C1000 170 820 170 560 185 C330 198 140 225 0 252 Z" fill="url(#topBand)"/>
    <path d="M0 592 C250 560 520 600 760 690 C900 738 1060 725 1200 690 V933 H0 Z" fill="url(#bottomBand)"/>
    <g stroke="#b9b9b9" stroke-width="1.2" stroke-dasharray="6 4" fill="none">
      <line x1="14" y1="18" x2="1186" y2="18"/>
      <line x1="14" y1="915" x2="1186" y2="915"/>
      <line x1="14" y1="18" x2="14" y2="590"/>
      <line x1="1186" y1="18" x2="1186" y2="690"/>
      <line x1="32" y1="36" x2="1168" y2="36"/>
      <line x1="32" y1="36" x2="32" y2="590"/>
    </g>
    <g stroke="#b9b9b9" stroke-width="1" opacity=".8">
      <line x1="400" y1="0" x2="400" y2="933"/>
      <line x1="793" y1="0" x2="793" y2="933"/>
    </g>
  </svg>

  <span class="guide-label" style="left:88px;top:4px;">Trim Line = final trim size ordered</span>
  <span class="guide-label" style="left:940px;top:20px;">Safety Line - no TEXT beyond this line</span>
  <span class="guide-label" style="left:958px;top:911px;">Trim Line = final trim size ordered</span>
  <span class="fold-label" style="left:394px;top:494px;">Fold Line</span>
  <span class="fold-label" style="left:787px;top:494px;">Fold Line</span>

  <svg class="photo" style="left:1030px;top:20px" width="135" height="228" role="img" aria-label="Photo of a young woman performing a breast self-exam">
    <rect width="135" height="228" fill="#c99a86"/>
  </svg>
  <svg class="photo" style="left:248px;top:224px" width="114" height="143" role="img" aria-label="Portrait of Dr. Mira Castellan">
    <rect width="114" height="143" fill="#5e6a83"/>
  </svg>
  <svg class="photo" style="left:480px;top:508px" width="240" height="402" role="img" aria-label="Photo of a serene woman hugging her shoulders">
    <rect width="240" height="402" fill="#b98a70"/>
  </svg>
  <svg class="photo" style="left:0;top:722px" width="212" height="190" role="img" aria-label="Photo of a pink lotus flower">
    <rect width="212" height="190" fill="url(#lotusTone)"/>
  </svg>
  <svg class="photo" style="left:860px;top:496px" width="236" height="206" role="img" aria-label="Photo of a hanging three-step breast self-check shower card">
    <rect width="236" height="206" fill="url(#cardTone)"/>
  </svg>

  <section class="panel panel-comprehensive">
    <p>(Comprehensive)<br>We provide a caring, intimate environment where your dignity and health come first. Conveniently, we are situated next to Linden Ridge Hospital, in the Harlow Whitcombe Cancer Center. This means that any necessary diagnostic and treatment modalities are at our fingertips.</p>
    <p>We understand the anxiety involved with breast problems. We know that when you are told that you need to be evaluated more closely, you want answers as quickly as possible. We are here to help you, striving to be as proficient as possible. Being dedicated to breast care, we have a wealth of up-to-date knowledge about current breast care concepts. Your doctor will listen to your concerns and work with you to make sure you understand your options.</p>
    <p>Our knowledgeable staff will help to alleviate your anxiety with timely appointments, education and compassion. We will make sure you have all the facts to make the best decisions about your health care.</p>
  </section>

  <section class="panel panel-personal">
    <p>(Personal)<br>Dr. Mira Castellan is the first fellowship-trained breast surgeon south of Maplewood, Ill., and is excited to come home and bring her expertise to the women of Southern Illinois.</p>
    <p>She deeply understands that you need to heal physically... emotionally... spiritually.</p>
    <p>This is truly comprehensive breast care.</p>
    <ul>
      <li>Services include:</li>
      <li>Breast pain and other nonsurgical management of breast problems</li>
      <li>Treatment of diseases of the breast (abscesses, gynecomastia)</li>
      <li>Biopsies (including minimally invasive with ultrasound or stereotactic guidance)</li>
      <li>Cryoablation (freezing) of certain breast conditions</li>
    </ul>
    <ul>
      <li>Breast resections (as needed for benign or malignant disease processes)</li>
      <li>Lymph node resections (including sentinel lymph node excisions)</li>
      <li>Breast reconstruction and balancing of the “other” breast as needed</li>
      <li>Breast reductions (for cancer or for burdensome breasts)</li>
      <li>Mastopexies (breast lifts for cancer or droopy breasts)</li>
    </ul>
    <p class="closing">Of course, this is not an exhaustive list. If there is a procedure you are interested in, please call our office to find out if we offer it.</p>
  </section>

  <section class="panel panel-timely">
    <p>(Timely)<br>Dedicated -- to bringing to you the most fresh and knowledgeable breast care, including all diagnostic studies and any surgical techniques necessary.<br>Unified team approach -- one that includes communication with your primary doctor, laboratory, radiology and ancillary services in a coordinated effort.<br>Appropriate resources -- including support groups, therapy, oncology, radiation oncology, cancer societies and more.</p>
    <p>Experience: Dr. Castellan has focused her entire practice on breast surgery, as she feels that this is the field in which she excels. Being fellowship-trained in Oncoplastic Breast Surgery, she intensely believes in comprehensive breast care and being with the patient through the entire experience. She is comfortable treating patients of all ages, from birth to the elderly. Being compassionate and caring, she strives to project these qualities into everything that she puts her hands on. Dr. Castellan is passionate about making sure that her patients get the best care, that they are well-informed, and treated with the dignity and respect that they deserve.</p>
  </section>

  <div class="brand">
    <span class="brand-mark" aria-hidden="true"></span>
    <span class="brand-name">Willowmere Surgery</span>
  </div>
  <div class="brand-tagline">Comprehensive Breast Care</div>

</div>
</body>
</html>
```